File your income taxes and walk away with cash today. direct mailer campaign

We prepare income tax returns. Our slogan is Walk away with cash today! Our marketing edge above our competition is the fact that clients can get up to $5000 the day they file. We also offer notary, payroll, and bookkeeping services. We would like something with cash on the card as well. Quill Ledger Returns is the name of our company and this campaign is actually for a direct mailer to client prospects that make under 25k a year, who will be looking for help preparing their income tax documents but also be looking for cash the same day they file. Our office will begin handing out checks on January 2nd!

Target Market(s)

My target market for this particular piece is Blacks and Hispanics of lower income.

Industry/Entity Type

Finance And Accounting

Font styles to use
Serif
Script

Colors
a54499
b768aa
33a6d7
33b8a4
e667a6
e34197

Requirements
Must have
• Quill Ledger Returns should be written is some form of script, prefer colors of Purple & aqua or Pink and Turquoise. Some form of cash that looks as real as possible.
Nice to have
• Here is our contact info:
• 412 North Caldwell Hammond Parkway
• Dallas, TX 75148
• (281) 555-0374
• www.quillledgerreturns.example
Should not have
• No white people or body parts

```html
<!DOCTYPE html>
<html lang="en">
<head>
<meta charset="utf-8">
<title>Quill Ledger Returns – Direct Mailer</title>
<link rel="stylesheet" href="https://fonts.googleapis.com/css2?family=Pinyon+Script&family=Open+Sans:ital,wght@0,700;1,700&display=swap">
<style>
  :root {
    --teal: #33b8a4;
    --pink: #e34197;
    --pink-soft: #f19ac4;
    --magenta: #a54499;
    --white: #ffffff;
    --stage: #f4e7ef;
    --script: "Pinyon Script", cursive;
    --sans: "Open Sans", sans-serif;
  }
  * { box-sizing: border-box; margin: 0; padding: 0; }
  html, body { width: 1200px; height: 696px; overflow: hidden; }
  body { background: var(--stage); position: relative; font-family: var(--sans); }

  .card {
    position: absolute;
    top: 161px;
    width: 560px;
    height: 374px;
    overflow: hidden;
    box-shadow: 0 6px 18px rgba(0,0,0,.18);
  }

  /* Front */
  .card-front { left: 27px; background: var(--white); }
  .front-pink-strip { position: absolute; left: 46px; top: 0; width: 14px; height: 100%; background: var(--pink-soft); }
  .front-teal { position: absolute; left: 60px; top: 0; right: 0; bottom: 0; background: var(--teal); }
  .front-name-box {
    position: absolute; left: 84px; top: 0; right: 14px; height: 92px;
    background: var(--white);
    display: flex; align-items: center; justify-content: center;
  }
  .brand-name { font-family: var(--script); color: var(--pink); font-weight: 400; line-height: 1; white-space: nowrap; }
  .front-name-box .brand-name { font-size: 46px; }
  .slogan { font-family: var(--script); color: var(--white); line-height: 1; white-space: nowrap; }
  .front-slogan { position: absolute; left: 84px; right: 14px; top: 96px; text-align: center; font-size: 30px; }
  .front-info-box {
    position: absolute; left: 84px; top: 134px; right: 14px; bottom: 22px;
    background: var(--white);
  }
  .contact { list-style: none; padding: 8px 0 0 12px; }
  .contact li {
    display: flex; align-items: center; gap: 6px;
    font-style: italic; font-weight: 700; font-size: 14px; color: var(--pink);
    line-height: 21px; white-space: nowrap;
  }
  .contact .pair { gap: 14px; }
  .contact .pair span { display: flex; align-items: center; gap: 6px; }
  .icon { width: 11px; height: 11px; flex: none; }
  .front-accent-bar { position: absolute; left: 0; top: 78px; width: 12px; bottom: 0; background: var(--pink); }
  .front-accent-line { position: absolute; left: 0; right: 0; bottom: 0; height: 10px; background: var(--pink); }
  .tax-art {
    position: absolute; left: 12px; top: 88px; right: 0; bottom: 10px;
    background: linear-gradient(90deg, #ffffff 0%, #e2e2e2 30%, #9a9a9a 55%, #a4417f 80%, #f6e6ef 100%);
  }

  /* Back */
  .card-back { left: 613px; background: var(--teal); }
  .back-header {
    position: absolute; left: 0; top: 40px; width: 392px; height: 78px;
    background: var(--white);
    display: flex; align-items: center; justify-content: center;
  }
  .back-header .brand-name { font-size: 40px; }
  .back-slogan { position: absolute; left: 14px; width: 380px; top: 124px; text-align: center; font-size: 28px; }
  .offer-box {
    position: absolute; left: 26px; top: 160px; width: 366px; height: 200px;
    background: var(--white); padding: 10px 16px 0 18px;
  }
  .offers { list-style: none; }
  .offers li {
    position: relative; padding-left: 14px;
    font-weight: 700; font-size: 14.5px; line-height: 18px; color: var(--teal);
  }
  .offers li::before {
    content: ""; position: absolute; left: 0; top: 6px;
    width: 8px; height: 8px; border-radius: 50%; background: var(--pink);
  }
  .extra-services {
    margin-top: 10px; text-align: center;
    font-weight: 700; font-size: 17px; line-height: 21px; color: var(--pink);
  }
  .back-column { position: absolute; left: 406px; top: 42px; width: 140px; bottom: 20px; background: var(--pink-soft); }
  .portrait {
    position: absolute; left: 14px; top: 0; right: 0; height: 150px;
    background: linear-gradient(160deg, #c9a57d 0%, #6b4633 45%, #3d2a3f 100%);
  }
  .practitioner { position: absolute; left: 14px; top: 150px; right: 0; height: 50px; background: var(--white); padding: 6px 6px 0; }
  .practitioner-name { font-family: var(--script); color: var(--teal); font-size: 19px; line-height: 1; white-space: nowrap; }
  .practitioner-role { font-size: 8.5px; color: var(--teal); font-style: italic; font-weight: 700; white-space: nowrap; }
  .clock-art {
    position: absolute; left: 14px; top: 200px; right: 0; bottom: 0;
    background: radial-gradient(circle at 45% 55%, #ffffff 0%, #f3f3f3 55%, #e6c9cf 100%);
  }
</style>
</head>
<body>

<section class="card card-front" aria-label="Mailer front">
  <div class="front-pink-strip"></div>
  <div class="front-teal"></div>
  <div class="front-name-box"><h1 class="brand-name">Quill Ledger Returns</h1></div>
  <p class="slogan front-slogan">Walk away with cash today !</p>
  <div class="front-info-box">
    <ul class="contact">
      <li>
        <svg class="icon" viewBox="0 0 12 12"><circle cx="6" cy="6" r="5.5" fill="none" stroke="#33b8a4"/><path d="M6 2.5a2 2 0 0 0-2 2c0 1.6 2 4 2 4s2-2.4 2-4a2 2 0 0 0-2-2z" fill="#33b8a4"/></svg>
        412 North Caldwell Hammond Parkway Dallas, TX 75148
      </li>
      <li class="pair">
        <span>
          <svg class="icon" viewBox="0 0 12 12"><circle cx="6" cy="6" r="5.5" fill="none" stroke="#33b8a4"/><path d="M4 3l1.2 1.6-.6.8a4 4 0 0 0 2 2l.8-.6L9 8l-.8.9C6 8.8 3.2 6 3.1 3.8z" fill="#33b8a4"/></svg>
          (281) 555-0374
        </span>
        <span>
          <svg class="icon" viewBox="0 0 12 12"><circle cx="6" cy="6" r="5.5" fill="#33b8a4"/><rect x="3" y="4" width="6" height="4.2" fill="#fff"/><path d="M3 4l3 2.3L9 4" fill="none" stroke="#33b8a4" stroke-width=".8"/></svg>
          www.quillledgerreturns.example
        </span>
      </li>
      <li>
        <svg class="icon" viewBox="0 0 12 12"><circle cx="6" cy="6" r="5.5" fill="#33b8a4"/></svg>
        @quillledgerreturns
      </li>
    </ul>
    <div class="tax-art" role="img" aria-label="Three-dimensional tax and taxation word cloud illustration"></div>
    <div class="front-accent-bar"></div>
    <div class="front-accent-line"></div>
  </div>
</section>

<section class="card card-back" aria-label="Mailer back">
  <div class="back-header"><h2 class="brand-name">Quill Ledger Returns</h2></div>
  <p class="slogan back-slogan">Walk away with cash today !</p>
  <div class="offer-box">
    <ul class="offers">
      <li>Up to $5000 Same day you file!</li>
      <li>We will get your maximum refund!</li>
      <li>Submit documents securely from your home!</li>
      <li>Our office will begin handing out checks on January 2nd!</li>
    </ul>
    <p class="extra-services">We also offer<br>Notary, Payroll,<br>Bookkeeping Services.</p>
  </div>
  <aside class="back-column">
    <div class="portrait" role="img" aria-label="Portrait photo of the tax practitioner"></div>
    <div class="practitioner">
      <p class="practitioner-name">Renata Okafor</p>
      <p class="practitioner-role">Manager, Tax Practitioner</p>
    </div>
    <div class="clock-art" role="img" aria-label="Clock illustration reading Time for taxes with a hand holding a red pin"></div>
  </aside>
</section>

</body>
</html>
```